A private security company called "Ventrell Security Services Ltd"

Hello everybody,

We need a web page for a company based in NZ. It is mainly an informative website so it would be wonderful if the designer puts their absolute best into making it a website that I would really appreciate. The website needs to show professionalism and also needs to make our web surfers find the information they need in a click. the company's colour is black and silver, and if those two colours could be integrated into the website it would be absolutely lovely. Please do contact me for any information.

Sincerely,
Dorian Valcourt

```html
<!DOCTYPE html>
<html lang="en">
<head>
<meta charset="utf-8">
<title>Ventrell Security Services Ltd</title>
<link href="https://fonts.googleapis.com/css2?family=Open+Sans:wght@400;600&display=swap" rel="stylesheet">
<style>
:root{
  --page-dark:#2a2a2a;
  --page-light:#e8e9ec;
  --white:#ffffff;
  --ink:#1c1c1c;
  --ink-soft:#555a60;
  --ink-muted:#6e7278;
  --rule:#d9dadd;
  --nav-top:#8d8f97;
  --nav-bottom:#6c6e76;
  --nav-active:#b9bbc1;
  --nav-dark:#2c2c2e;
  --silver:#c9cbd0;
  --accent-red:#d62a22;
  --footer-band:#232323;
}
*{box-sizing:border-box;margin:0;padding:0}
html,body{width:982px;height:1200px;overflow:hidden}
body{font-family:"Open Sans",sans-serif;background:var(--page-light);position:relative;color:var(--ink)}
.top-band{position:absolute;left:0;top:0;width:982px;height:525px;background:var(--page-dark)}
.sheet{position:absolute;left:81px;top:26px;width:820px;height:915px;background:var(--white)}
.abs{position:absolute}

/* header */
.brand{left:90px;top:64px;display:flex;align-items:center;gap:10px}
.brand-mark{width:34px;height:34px;border-radius:50%;background:var(--ink)}
.brand-name{font-size:17px;font-weight:600;color:var(--ink);line-height:1.15;letter-spacing:.5px}
.social-top{left:812px;top:48px;display:flex;gap:12px}
.social-top span{width:16px;height:16px;border-radius:50%;background:#444}
.contact-block{top:97px;text-align:right}
.contact-label{font-size:12px;color:var(--ink-soft)}
.contact-value{font-size:16px;color:var(--ink);margin-top:1px}
.contact-email{right:262px}
.contact-phone{right:142px}
.v-rule{width:1px;height:38px;background:var(--rule);top:97px}
.phone-icon{left:864px;top:104px}

/* nav */
.main-nav{left:89px;top:160px;width:804px;height:39px;display:flex;background:linear-gradient(var(--nav-top),var(--nav-bottom))}
.main-nav a{display:flex;align-items:center;justify-content:center;font-size:12px;color:#fff;text-decoration:none;border-right:1px solid #5e6067}
.main-nav .is-active{background:var(--nav-active);color:var(--ink)}
.main-nav .nav-enquire{background:var(--nav-dark);border-right:0}

/* hero */
.hero{left:89px;top:204px;width:804px;height:321px;background:linear-gradient(90deg,#dcdde0 0%,#ececee 45%,#d8d9dc 75%,#b9bbc0 100%)}
.hero-caption{left:89px;top:441px;width:308px;height:38px;background:rgba(45,45,47,.92);color:#fff;font-size:20px;display:flex;align-items:center;padding-left:18px}
.hero-arrow{top:331px;width:20px;height:68px;background:#fff;display:flex;align-items:center;justify-content:center}
.hero-arrow-left{left:89px;border-radius:0 40px 40px 0}
.hero-arrow-right{left:873px;border-radius:40px 0 0 40px}

/* features */
.feature-title{top:545px;width:255px;text-align:center;font-size:16px;color:#3a3c40}
.feature-image{top:573px;width:255px;height:136px}
.img-products{background:linear-gradient(135deg,#e4edf0,#a9bcc4 60%,#dfe6e8)}
.img-guard{background:radial-gradient(circle at 50% 45%,#3d4458,#0e0f14 70%)}
.img-alarm{background:linear-gradient(90deg,#e9dfe0,#f2eef0 50%,#d63a35 85%,#e7e4e5)}
.divider{left:89px;top:736px;width:804px;height:1px;background:var(--rule)}

/* welcome */
.welcome-title{left:90px;top:754px;font-size:22px;font-weight:400;color:var(--ink)}
.welcome-lead{left:90px;top:793px;width:590px;font-size:13px;line-height:19px;color:var(--ink)}
.welcome-body{left:90px;top:842px;width:600px;font-size:11px;line-height:19px;color:var(--ink-muted)}
.video{left:705px;top:793px;width:187px;height:119px;background:linear-gradient(90deg,#5b4b44,#8a8988 55%,#4d5660)}
.play{left:783px;top:838px;width:30px;height:28px;background:var(--accent-red);border-radius:4px;display:flex;align-items:center;justify-content:center}

/* footer */
.footer-heading{top:967px;font-size:13px;font-weight:600;color:#2f3134}
.footer-list{top:995px;list-style:none;font-size:10.5px;line-height:20.5px;color:var(--ink-soft)}
.footer-address{left:476px;top:996px;font-size:10.5px;line-height:15.5px;color:var(--ink-soft)}
.directions{left:476px;top:1053px;display:flex;align-items:center;gap:8px;font-size:10.5px;color:var(--ink-soft)}
.social-foot{left:100px;top:1100px;display:flex;gap:4px}
.social-foot span{width:24px;height:24px;border:1px solid #c3c5c9;background:#f7f7f8;border-radius:3px;display:flex;align-items:center;justify-content:center}
.social-foot span::after{content:"";width:9px;height:9px;border-radius:50%;background:#777}
.field{left:636px;width:188px;background:#fff;border:1px solid #d7d8dc;border-radius:3px;font-size:10.5px;color:#333;padding:8px 10px}
.submit{left:832px;top:1099px;width:53px;height:26px;background:#4a4c50;color:#fff;font-size:10.5px;border-radius:3px;display:flex;align-items:center;justify-content:center}
.footer-band{left:0;top:1151px;width:982px;height:49px;background:var(--footer-band)}
.copyright{left:0;top:1167px;width:982px;text-align:center;font-size:10.5px;color:#a9abaf}
</style>
</head>
<body>
<div class="top-band"></div>
<div class="sheet"></div>

<header>
  <div class="abs brand">
    <span class="brand-mark"></span>
    <span class="brand-name">Ventrell<br>Security Services Ltd</span>
  </div>
  <div class="abs social-top" aria-label="Social links"><span></span><span></span><span></span></div>
  <div class="abs contact-block contact-email"><div class="contact-label">E-mail</div><div class="contact-value">info@ventrellss.com</div></div>
  <div class="abs v-rule" style="left:732px"></div>
  <div class="abs contact-block contact-phone"><div class="contact-label">Call us</div><div class="contact-value">456 321 7720</div></div>
  <div class="abs v-rule" style="left:852px"></div>
  <svg class="abs phone-icon" width="26" height="22" viewBox="0 0 26 22" aria-hidden="true">
    <path d="M4 3c2-1 3 0 4 2l1 3c0 1-1 2-2 2 1 3 3 5 6 6 0-1 1-2 2-2l3 1c2 1 3 2 2 4-1 2-3 3-6 2C8 19 3 13 2 8 1 6 2 4 4 3z" fill="#2b2b2b"/>
    <path d="M17 4a6 6 0 0 1 5 5M17 7a3 3 0 0 1 2 2" stroke="#777" stroke-width="1.4" fill="none"/>
  </svg>
</header>

<nav class="abs main-nav">
  <a class="is-active" style="width:84px">HOME</a>
  <a style="width:110px">ABOUT US</a>
  <a style="width:98px">SERVICES</a>
  <a style="width:122px">GUARDS FOR</a>
  <a style="width:141px">NEWS &amp; EVENTS</a>
  <a style="width:118px">CONTACT US</a>
  <a class="nav-enquire" style="width:131px">ENQUIRE NOW</a>
</nav>

<section>
  <div class="abs hero" role="img" aria-label="Uniformed security officer standing in a bright office lobby"></div>
  <div class="abs hero-caption">Aliquam auctor luctus diam.</div>
  <div class="abs hero-arrow hero-arrow-left"><svg width="8" height="12" viewBox="0 0 8 12"><path d="M6 1 1 6l5 5" stroke="#333" stroke-width="2" fill="none"/></svg></div>
  <div class="abs hero-arrow hero-arrow-right"><svg width="8" height="12" viewBox="0 0 8 12"><path d="M2 1l5 5-5 5" stroke="#333" stroke-width="2" fill="none"/></svg></div>
</section>

<section>
  <h3 class="abs feature-title" style="left:90px;font-weight:400">Security Products</h3>
  <div class="abs feature-image img-products" style="left:90px" role="img" aria-label="Ceiling-mounted security camera"></div>
  <h3 class="abs feature-title" style="left:364px;font-weight:400">Guard Service</h3>
  <div class="abs feature-image img-guard" style="left:364px" role="img" aria-label="Security guard in dark uniform and cap"></div>
  <h3 class="abs feature-title" style="left:637px;font-weight:400">Alarm Technolgoy</h3>
  <div class="abs feature-image img-alarm" style="left:637px" role="img" aria-label="Red fire alarm bell on a shopping mall wall"></div>
  <div class="abs divider"></div>
</section>

<section>
  <h1 class="abs welcome-title">Welcome Ventrell Security Services Ltd.</h1>
  <p class="abs welcome-lead">Sed pellentesque enim eget eros malesuada, non placerat nibh euismod. Morbi eu justo convallis, euismod risus quis, posuere purus.</p>
  <p class="abs welcome-body">Fusce vel nunc lacinia, molestie est et, molestie diam. In malesuada scelerisque pulvinar. Aliquam ut quam eget sem consectetur laoreet. Cras bibendum metus eget tortor faucibus, a suscipit eros pellentesque. Aliquam auctor luctus diam, in condimentum velit placerat in. Aenean quam augue, consequat vitae urna nec, pellentesque tempus nunc. Quisque vitae accumsan magna. Praesent leo augue, pulvinar ut ligula eu, iaculis suscipit lectus.</p>
  <div class="abs video" role="img" aria-label="Video still of a digital eye scan"></div>
  <div class="abs play"><svg width="12" height="14" viewBox="0 0 12 14"><path d="M1 1l10 6-10 6z" fill="#fff"/></svg></div>
</section>

<footer>
  <h4 class="abs footer-heading" style="left:99px">Navigation Menu</h4>
  <ul class="abs footer-list" style="left:99px"><li>Home</li><li>About us</li><li>Services</li><li>Guards for</li></ul>
  <ul class="abs footer-list" style="left:185px"><li>News &amp; Events</li><li>Contact us</li><li>Enquire Now</li></ul>
  <h4 class="abs footer-heading" style="left:313px">Support Links</h4>
  <ul class="abs footer-list" style="left:313px"><li>Privacy Policy</li><li>Terms and Conditions</li><li>Customer Support</li><li>FAQ</li></ul>
  <h4 class="abs footer-heading" style="left:476px">Contact us</h4>
  <p class="abs footer-address">55, Building name<br>Street name, City<br>Zip code</p>
  <div class="abs directions">
    <svg width="22" height="22" viewBox="0 0 22 22" aria-hidden="true"><rect x="1" y="3" width="20" height="18" rx="2" fill="#3a3c40"/><path d="M7 8a3 3 0 1 1 0 .1M7 11v6M15 7v10" stroke="#fff" stroke-width="1.6" fill="none"/></svg>
    Get Directions
  </div>
  <div class="abs social-foot" aria-label="Social links"><span></span><span></span><span></span></div>
  <h4 class="abs footer-heading" style="left:638px">Contact us</h4>
  <div class="abs field" style="top:1003px;height:28px">Name</div>
  <div class="abs field" style="top:1037px;height:28px">E-mail</div>
  <div class="abs field" style="top:1071px;height:54px">Comment</div>
  <div class="abs submit">SUBMIT</div>
  <div class="abs footer-band"></div>
  <p class="abs copyright">Copyright &copy; 2014 &nbsp;Ventrell Security Services Ltd. &nbsp; All rights reserved.</p>
</footer>
</body>
</html>
```